Glenmoor Vale Executive Development Workshop Series

* Had error in first version of MS Word doc and have re-uploaded - twelve subject areas, not nine *
I'd like a flyer to print to hand out and post on my website glenmoorvale.com to advertise a workshop series I'm launching. I'd like it to build strongly on the wonderful logo you did and Scottish theme...and to have the same "feel" as my website. glenmoorvale.com
It should be 8.5x11, single sided. Not sure if I should use full color glossy or two-color on nice paper. Regardless, I will most likely have it done on a color copier and will not put it on a printing press.
I have typed up a document with all the information in a MS Word file, but need you to lay it out in an aesthetically pleasing way. I have attached that MS Word file.
I am also attaching a handful of similar flyer documents from other non-competing coaches in my network. I think they all have their merits, but leave me under-whelmed.
I'm also attaching a picture of me and some pictures of Scotland my parents took about 10 years ago. I'm reluctantly open to stock photos, just not too obvious or hackneyed (if that word can be applied to pictures as well as expressions).
Lastly, this workshop series will be an ongoing thing, so I'd like to be able to make minor edits myself with things like new dates or topics.
Thank you!
Target Market(s)
Small business owners and emerging leaders with large companies
Colors
Designer to choose colors to be used in the design.
Requirements
Should not have
- Obviously stock photos

```html
<!DOCTYPE html>
<html lang="en">
<head>
<meta charset="utf-8">
<title>Glenmoor Vale Executive Development Workshop Series</title>
<link href="https://fonts.googleapis.com/css2?family=Cinzel:wght@400;500&family=Lato:wght@300;400;700&display=swap" rel="stylesheet">
<style>
:root{
  --olive:#3f4a24;
  --olive-dark:#2f3a1c;
  --ink:#2b2b2b;
  --text:#333;
  --band:#c4d49c;
  --band-light:#e4ecd0;
  --header-bg:#f1f1f1;
  --footer:#262626;
  --stage:#e8e8e8;
  --bullet-light:#b9cc8c;
}
*{box-sizing:border-box;margin:0;padding:0}
html,body{width:1200px;height:1200px;overflow:hidden;background:var(--stage)}
body{font-family:"Lato",sans-serif;color:var(--text)}
.flyer{position:absolute;left:133px;top:0;width:933px;height:1200px;background:#fff;overflow:hidden}
.hero{position:absolute;left:0;top:0;width:933px;height:243px;
  background:linear-gradient(180deg,#c9cccc 0%,#b3b8b3 45%,#7e8a6c 80%,#5e6b45 100%)}
.brand-mark{position:absolute;left:33px;top:33px;width:128px;height:126px;background:var(--olive);
  display:flex;align-items:center;justify-content:center;color:#fff;font-size:15px;font-weight:400;letter-spacing:1px;text-align:center}
.rule{position:absolute;left:0;width:933px}
.rule.thin{top:245px;height:2px;background:var(--olive)}
.rule.thick{top:249px;height:4px;background:var(--olive)}
.title-band{position:absolute;left:0;top:253px;width:933px;height:109px;background:var(--header-bg)}
.title-line1{position:absolute;left:36px;top:272px;font-size:27px;line-height:30px;font-weight:400;color:var(--olive);letter-spacing:.2px}
.title-line2{position:absolute;left:36px;top:306px;font-family:"Cinzel",serif;font-size:29px;line-height:34px;font-weight:400;color:var(--olive);letter-spacing:1px;white-space:nowrap}
.intro{position:absolute;left:33px;top:382px;width:870px;font-size:12.8px;line-height:16px;color:var(--ink)}
.band{position:absolute;left:0;background:var(--band);color:var(--olive-dark);font-weight:700}
.band.topics{top:444px;height:47px;width:733px;clip-path:polygon(0 0,100% 0,98.4% 100%,0 100%);font-size:13px;line-height:16px;padding:6px 0 0 33px}
.band.includes{top:859px;height:25px;width:368px;clip-path:polygon(0 0,100% 0,96% 100%,0 100%);font-size:13px;padding:5px 0 0 33px}
.topics-col{position:absolute;top:513px;list-style:none}
.topics-col.left{left:33px;width:420px}
.topics-col.right{left:474px;width:440px}
.topic{position:relative;padding-left:18px;margin-bottom:13.5px}
.topic::before{content:"";position:absolute;left:0;top:7px;width:7px;height:7px;border-radius:50%;background:var(--ink)}
.topic h3{font-size:16px;font-weight:700;color:var(--ink);line-height:21px}
.topic p{position:relative;font-size:13px;line-height:16px;color:var(--ink);padding-left:12px;margin-top:3px}
.topic p::before{content:"";position:absolute;left:0;top:6px;width:4px;height:4px;background:var(--ink)}
.includes-list{position:absolute;left:33px;top:893px;width:421px;list-style:none}
.includes-list li{position:relative;padding-left:20px;font-size:12.5px;line-height:16px;color:var(--ink);text-align:justify;margin-bottom:10px}
.includes-list li::before{content:"";position:absolute;left:1px;top:5px;width:7px;height:7px;border-radius:50%;background:var(--bullet-light)}
.includes-list strong{font-size:14px}
.register{position:absolute;left:470px;top:838px;width:463px;height:258px;
  background:linear-gradient(90deg,#c4d49c 0%,#e8eed6 100%);padding:16px 18px 0 37px;color:var(--ink)}
.register .lead{font-size:13px;line-height:16px}
.register .lead strong{font-size:16px}
.register .price{font-size:30px;line-height:34px;margin-top:6px;white-space:nowrap}
.register .terms{font-size:22px;line-height:26px;margin-left:-2px;white-space:nowrap}
.register .note{font-size:12.8px;line-height:16px;margin-top:8px}
.register .note + .note{margin-top:14px}
.footer{position:absolute;left:0;top:1088px;width:933px;height:112px}
.footer-contact{position:absolute;left:33px;top:1097px;color:#fff}
.footer-contact .name{font-size:19px;font-weight:300}
.footer-contact .row{display:flex;align-items:center;font-size:19px;font-weight:300;margin-top:2px}
.footer-contact .row svg{margin-right:6px}
.footer-contact .gap{margin-left:30px}
.footer-contact .site{letter-spacing:3px;font-size:17px}
.member-badge{position:absolute;left:695px;top:1104px;width:48px;height:74px}
</style>
</head>
<body>
<div class="flyer">
  <div class="hero" role="img" aria-label="Misty Scottish highland glen with mountains under low clouds"></div>
  <div class="brand-mark">Glenmoor Vale</div>
  <div class="rule thin"></div>
  <div class="rule thick"></div>

  <div class="title-band"></div>
  <h1 class="title-line1">GLENMOOR VALE EXECUTIVE</h1>
  <h2 class="title-line2">Development Workshop Series - First Thursdays</h2>

  <p class="intro">A positive, fresh, results-driven approach for businesses to increase profits by building confidence, command and control in owners and executives. We will use proven leadership and business strategies to improve work-life balance, buy-in, and company value. Here’s your opportunity to meet with other like-minded business owners and executives once a month in a private and confidential setting</p>

  <div class="band topics">We’ve got nine subject areas planned, and while they are all powerful, we will shift from high-level strategy topics to “WHERE THE RUBBER MEETS THE ROAD” topics.</div>

  <ul class="topics-col left">
    <li class="topic"><h3>Sep 7 – My Company Owns Me :</h3><p>What a CEO should and should not do</p></li>
    <li class="topic"><h3>Oct 5 – Taking Vision / Mission / Values</h3><p>Down To The Molecular Level Of Your Company</p></li>
    <li class="topic"><h3>Nov 2 – People Problems</h3><p>The biggest waste of time and money for every small business</p></li>
    <li class="topic"><h3>Dec 7 – Value Delivery Systems</h3><p>Re-think everything you think you know about creating value</p></li>
    <li class="topic"><h3>Jan 4, 2018 – Rally Your Team Around A Goal</h3><p>How to create a meaningful company goal<br>and rally the troops around it</p></li>
    <li class="topic"><h3>Feb 1 – Building Your Executive Leadership Team</h3><p>You can’t succeed without one</p></li>
  </ul>

  <ul class="topics-col right">
    <li class="topic"><h3>Mar 1 – Improve Your Outside Sales Efforts</h3><p>Help your sales force to be busy AND successful</p></li>
    <li class="topic"><h3>Apr 5 – Every Brain In The Game</h3><p>Engage your team and build a strong culture</p></li>
    <li class="topic"><h3>May 3 – Repeatable Processes</h3><p>Coach your employees how to get predictable results every time</p></li>
    <li class="topic"><h3>Jun 7 – Finding and Filling Profit Holes</h3><p>Most small businesses waste more money than they profit</p></li>
    <li class="topic"><h3>*Jul 12 – Put Your Payroll On A Diet</h3><p>Why waste happens, what to do about it and how it helps everyone</p></li>
    <li class="topic"><h3>Aug 2 – Truly, How Effective Are You</h3><p>With This Whole “Leadership” Thing?</p></li>
  </ul>

  <div class="band includes">Each month of this monthly workshop series includes:</div>
  <ul class="includes-list">
    <li><strong>3-Hour Intensive Workshop:</strong> High-energy, creative sessions with engaging and relevant business topics, peer group advisory board (master mind), and networking (9am – 12pm, dates above)</li>
    <li><strong>90-minute one-on-one coaching session:</strong> to help you absorb and apply the revelations from the group sessions to your own business (mutually scheduled)</li>
    <li><strong>Participation and trust is vital to your investment</strong>; no holding back. Due to the confidential nature of the intensive workshops, all participants will sign a confidentiality agreement. Additionally, we will only allow one company per industry to be represented.</li>
  </ul>

  <section class="register">
    <p class="lead">To register, go to <strong>glenmoorvale.com/exec-dev</strong> and click the registration link</p>
    <p class="price">$395/month or $295/month</p>
    <p class="terms">with a 6-month or greater commitment</p>
    <p class="note">All monthly Intensive Workshops will be 9am – 12pm on the dates above at Ironwood Coworking at 212 Market Street, Winston-Salem NC 27101</p>
    <p class="note">All one-on-one coaching sessions will be mutually scheduled with Ian Dunmore once you have registered</p>
  </section>

  <svg class="footer" viewBox="0 0 933 112" aria-hidden="true">
    <polygon points="0,0 454,0 516,94 933,94 933,112 0,112" fill="#262626"/>
  </svg>
  <div class="footer-contact">
    <p class="name">Ian Dunmore, Certified Professional Business Coach</p>
    <p class="row">
      <svg width="18" height="18" viewBox="0 0 18 18"><circle cx="9" cy="9" r="8.5" fill="#fff"/><path d="M6 4.5l2 2-1 1.5c.7 1.4 1.6 2.3 3 3l1.5-1 2 2-1.3 1.5c-3.5-.4-6.3-3.2-6.7-6.7z" fill="#262626"/></svg>
      ian@glenmoorvale.com
      <svg class="gap" width="20" height="14" viewBox="0 0 20 14"><rect x="1" y="1" width="18" height="12" fill="none" stroke="#fff" stroke-width="1.6"/><path d="M1 1l9 7 9-7" fill="none" stroke="#fff" stroke-width="1.6"/></svg>
      336-555-0148
    </p>
    <p class="row site">
      <svg width="18" height="18" viewBox="0 0 18 18"><circle cx="9" cy="9" r="8" fill="none" stroke="#fff" stroke-width="1.5"/><ellipse cx="9" cy="9" rx="3.5" ry="8" fill="none" stroke="#fff" stroke-width="1.2"/><path d="M1 9h16M2.5 5h13M2.5 13h13" stroke="#fff" stroke-width="1.2"/></svg>
      glenmoorvale.com
    </p>
  </div>

  <svg class="member-badge" viewBox="0 0 48 74" aria-hidden="true">
    <path d="M2 2h44v38c0 12-10 20-22 24C12 60 2 52 2 40z" fill="#5b2d6e"/>
    <rect x="8" y="67" width="32" height="6" fill="#cfcfcf"/>
  </svg>
</div>
</body>
</html>
```